New business card for our new logo

I have a brand new, existing logo. Now I need it on a new business card. The new card should include the following:

English language training
Translations
Interpreting Services (remote and in-person)

Target Market(s)

We are targeting international companies with foreign investment in the United States as well as domestic companies, medical offices, law offices, and non-profits that have non-native English speakers as their clients.

Contact Information for Business Card

Marla Quennet, President
418 Garvin St.
Indianapolis, IN 46871
(317) 584-2316
info@brightpathwordworks.com
www.brightpathwordworks.com

Font styles to use
Sans Serif

Colors
0392cd
3176b5
abd036
9bcb3b
f04a50
f78f20

Requirements
Must have
• It must include our logo and business card details
Nice to have
• I would like to see a layout that is uncluttered and conveys trust and dependability, as well as the feelings of being friendly and approachable.

It would be nice to have icons for English language training, translating, and interpreting.
Should not have
• No pink, yellow, or purple

```html
<!DOCTYPE html>
<html lang="en">
<head>
<meta charset="utf-8">
<title>Brightpath Wordworks — Business Card</title>
<link href="https://fonts.googleapis.com/css2?family=Montserrat:wght@600;700&family=Lato:wght@400;700&display=swap" rel="stylesheet">
<style>
  :root {
    --backdrop: #d3d4cf;
    --card-white: #ffffff;
    --brand-blue: #3a6bb3;
    --brand-blue-deep: #2f5ea3;
    --text-grey: #5a5d63;
    --text-white: #ffffff;
  }
  * { box-sizing: border-box; margin: 0; padding: 0; }
  html, body {
    width: 1200px; height: 801px; overflow: hidden;
    background: var(--backdrop);
  }
  .stage {
    width: 1200px; height: 801px;
    display: flex; align-items: center; justify-content: center; gap: 48px;
  }
  .card {
    position: relative;
    width: 530px; height: 303px;
    box-shadow: 0 14px 28px rgba(0,0,0,.22);
    overflow: hidden;
  }

  /* Front */
  .card-front {
    background: var(--card-white);
    border-bottom: 4px solid var(--brand-blue);
  }
  .brand {
    display: flex; align-items: center; gap: 12px;
  }
  .brand-dot {
    width: 62px; height: 62px; border-radius: 50%;
    flex: none;
  }
  .brand-name {
    font-family: "Montserrat", sans-serif;
    font-weight: 700;
    font-size: 21px; line-height: 1.02;
  }
  .card-front .brand { position: absolute; left: 34px; top: 44px; }
  .card-front .brand-dot { background: var(--brand-blue); }
  .card-front .brand-name { color: var(--brand-blue); }

  .holder {
    position: absolute; right: 34px; top: 56px; text-align: right;
  }
  .holder-name {
    font-family: "Montserrat", sans-serif; font-weight: 700;
    font-size: 26px; color: var(--brand-blue); letter-spacing: -.3px;
  }
  .holder-title {
    font-family: "Lato", sans-serif; font-size: 14px; color: var(--text-grey);
    margin-top: 2px;
  }
  .divider {
    position: absolute; left: 34px; right: 34px; top: 152px;
    height: 1.5px; background: var(--brand-blue);
  }
  .contact-list {
    position: absolute; left: 34px; top: 176px;
    list-style: none;
    font-family: "Lato", sans-serif; font-size: 14px; color: var(--text-grey);
  }
  .contact-list li {
    display: flex; align-items: center; gap: 10px; height: 26px;
  }
  .contact-list svg { width: 16px; height: 16px; flex: none; }
  .address {
    position: absolute; right: 34px; top: 182px; text-align: right;
    font-family: "Lato", sans-serif; font-size: 14px; line-height: 1.6;
    color: var(--text-grey); font-style: normal;
  }

  /* Back */
  .card-back { background: var(--brand-blue); }
  .card-back .brand {
    position: absolute; left: 0; right: 0; top: 40px; justify-content: center;
  }
  .card-back .brand-dot { background: var(--card-white); width: 70px; height: 70px; }
  .card-back .brand-name { color: var(--text-white); font-size: 23px; }

  .service-list {
    position: absolute; left: 20px; right: 20px; top: 160px;
    display: flex; justify-content: space-around; list-style: none;
  }
  .service {
    width: 150px; text-align: center;
    font-family: "Lato", sans-serif; font-size: 14.5px; color: var(--text-white);
    line-height: 1.2;
  }
  .service-icon {
    width: 52px; height: 52px; margin: 0 auto 12px;
    border-radius: 8px;
    background: linear-gradient(160deg, rgba(255,255,255,.32), rgba(255,255,255,.16));
  }
</style>
</head>
<body>
<main class="stage">

  <section class="card card-front" aria-label="Business card front">
    <div class="brand">
      <span class="brand-dot" aria-hidden="true"></span>
      <span class="brand-name">Brightpath<br>Wordworks</span>
    </div>

    <div class="holder">
      <p class="holder-name">Marla Quennet</p>
      <p class="holder-title">President</p>
    </div>

    <div class="divider" aria-hidden="true"></div>

    <ul class="contact-list">
      <li>
        <svg viewBox="0 0 16 16" aria-hidden="true"><path d="M4 1.5l2.3 2.8-1.4 1.6c.9 2 2.3 3.4 4.3 4.3l1.6-1.4 2.8 2.3-1.4 2.2C7.4 13 3 8.6 1.8 3z" fill="#3a6bb3"/></svg>
        (317) 584-2316
      </li>
      <li>
        <svg viewBox="0 0 16 16" aria-hidden="true"><rect x="1" y="3" width="14" height="10" rx="1" fill="#3a6bb3"/><path d="M1.5 3.5L8 9l6.5-5.5" stroke="#fff" stroke-width="1.2" fill="none"/></svg>
        info@brightpathwordworks.com
      </li>
      <li>
        <svg viewBox="0 0 16 16" aria-hidden="true"><g fill="none" stroke="#3a6bb3" stroke-width="1.2"><circle cx="8" cy="8" r="6.5"/><ellipse cx="8" cy="8" rx="2.8" ry="6.5"/><path d="M1.5 8h13M2.5 5h11M2.5 11h11"/></g></svg>
        www.brightpathwordworks.com
      </li>
    </ul>

    <address class="address">
      418 Garvin St.<br>
      Indianapolis, IN 46871
    </address>
  </section>

  <section class="card card-back" aria-label="Business card back">
    <div class="brand">
      <span class="brand-dot" aria-hidden="true"></span>
      <span class="brand-name">Brightpath<br>Wordworks</span>
    </div>

    <ul class="service-list">
      <li class="service">
        <div class="service-icon" role="img" aria-label="Line icon of a teacher at a presentation board"></div>
        English language<br>training
      </li>
      <li class="service">
        <div class="service-icon" role="img" aria-label="Line icon of two speech bubbles exchanging characters"></div>
        Translations
      </li>
      <li class="service">
        <div class="service-icon" role="img" aria-label="Line icon of an interpreter between two people"></div>
        Interpreting Services
      </li>
    </ul>
  </section>

</main>
</body>
</html>
```